Business Flyer

I want an updated flyer that will have the same content as the one attached but in a different format. They flyers will be passed out to the community and local businesses.

```html
<!DOCTYPE html>
<html lang="en">
<head>
<meta charset="utf-8">
<title>Whirl Juice Bar Flyer</title>
<link rel="stylesheet" href="https://fonts.googleapis.com/css2?family=Dosis:wght@400;500&family=Roboto+Condensed:wght@300;400&display=swap">
<style>
  :root {
    --paper: #f8f7f9;
    --green: #7aa432;
    --orange: #f39a1e;
    --purple: #8a1e8c;
    --ink: #262626;
    --band: #e7e2ee;
    --pin: #e53935;
  }
  * { margin: 0; padding: 0; box-sizing: border-box; }
  html, body { width: 960px; height: 1200px; overflow: hidden; background: var(--paper); }
  .flyer {
    position: relative;
    width: 960px;
    height: 1200px;
    background: var(--paper);
    font-family: "Roboto Condensed", sans-serif;
    color: var(--ink);
  }
  .brand {
    position: absolute;
    left: 44px;
    top: 82px;
    display: flex;
    align-items: center;
    gap: 14px;
  }
  .brand-dot {
    width: 54px;
    height: 54px;
    border-radius: 50%;
    background: var(--purple);
  }
  .brand-name {
    font-family: "Dosis", sans-serif;
    font-weight: 500;
    font-size: 40px;
    color: var(--purple);
    letter-spacing: 1px;
    line-height: 1;
  }
  .headline {
    position: absolute;
    right: 46px;
    top: 56px;
    text-align: right;
    font-family: "Dosis", sans-serif;
    font-size: 50px;
    line-height: 46px;
    text-transform: uppercase;
  }
  .headline .line-green { color: var(--green); font-weight: 400; }
  .headline .line-orange { color: var(--orange); font-weight: 500; }
  .headline .line-purple { color: var(--purple); font-weight: 500; }
  .hero {
    position: absolute;
    left: 193px;
    top: 212px;
    width: 668px;
    height: 720px;
    border-radius: 40% 40% 30% 30%;
    background:
      radial-gradient(ellipse at 42% 28%, #f7b63b 0%, #f39a1e 28%, transparent 50%),
      radial-gradient(ellipse at 78% 42%, #8e2a4d 0%, transparent 32%),
      radial-gradient(ellipse at 40% 86%, #6c2a3a 0%, transparent 42%),
      radial-gradient(ellipse at 62% 68%, #d63a2c 0%, transparent 38%),
      radial-gradient(ellipse at 34% 64%, #5f8e2c 0%, transparent 34%),
      var(--paper);
  }
  .message {
    position: absolute;
    left: 120px;
    right: 120px;
    top: 966px;
    text-align: center;
    font-size: 20px;
    line-height: 26px;
    font-weight: 400;
  }
  .message .soft { font-weight: 300; }
  .contact-band {
    position: absolute;
    left: 0;
    bottom: 0;
    width: 960px;
    height: 76px;
    background: var(--band);
    display: flex;
    align-items: center;
    font-size: 19px;
  }
  .contact-item {
    position: absolute;
    display: flex;
    align-items: center;
    gap: 10px;
  }
  .contact-address { left: 48px; }
  .contact-social { left: 440px; }
  .contact-page { left: 720px; }
  .icon-square {
    width: 26px;
    height: 26px;
    border-radius: 5px;
    background: var(--purple);
  }
</style>
</head>
<body>
  <main class="flyer">
    <div class="brand">
      <span class="brand-dot"></span>
      <span class="brand-name">WHIRL JUICE BAR</span>
    </div>

    <h1 class="headline">
      <span class="line-green">Natural&nbsp; Cold Press</span><br>
      <span class="line-orange">Juices and Delicious</span><br>
      <span class="line-purple">Smoothies</span>
    </h1>

    <div class="hero" role="img" aria-label="Glass of orange juice with a splash and rosemary, a berry smoothie glass, and a pile of pineapple, kiwi, strawberries, orange halves and grapes"></div>

    <p class="message">
      <span class="soft">Thank you for supporting your loca l business as we aim to</span> provide you with a comfortable and inviting place coupled with great products that is conducive to changing people's lives and creating a positive community through our offerings of natural cold press juices and delicious smoothies!
    </p>

    <footer class="contact-band">
      <div class="contact-item contact-address">
        <svg width="22" height="28" viewBox="0 0 22 28" aria-hidden="true">
          <path d="M11 1C5.5 1 1 5.3 1 10.7 1 18 11 27 11 27s10-9 10-16.3C21 5.3 16.5 1 11 1z" fill="var(--pin)"/>
          <circle cx="11" cy="10.5" r="3.8" fill="#fff"/>
        </svg>
        <span>4187 Market Lane Brookfield MD 20744</span>
      </div>
      <div class="contact-item contact-social">
        <span class="icon-square"></span>
        <span>WHIRL_JUICE_BAR</span>
      </div>
      <div class="contact-item contact-page">
        <span class="icon-square"></span>
        <span>Whirl Juice Bar</span>
      </div>
    </footer>
  </main>
</body>
</html>
```